Podcast Cover Art for Fast Growing Show (Ill include a gracious tip!)

This artwork is for "The Steadfast Fellow Show." The podcast is for men, and it's all about self-improvement, confidence, success, money, women and masculinity. It's for the guy who wants to improve himself. I'd like for my picture to be included — in black and white — and I want the text to read: "The Steadfast Fellow Show" and somewhere in there it'll say: "with Dale Prowen." I'm open to color schemes. The podcast is a little edgy so I'd like for that to be represented in the design. Thank you! (((Here's the podcast page if you wanna check it out: http://steadfastfellowshow.castorbit.net/)))

Target Market(s)

Men who want to attract women and improve their lives!

Font styles to use
Serif

Colors

Designer to choose colors to be used in the design.

Requirements
Must have
• My image in it (in black and white) and the two titles: "The Steadfast Fellow Show" and "with Dale Prowen"
Nice to have
• My logo in it somehow (which is the arrow looking logo attached below). I've also found that my image looks best in black and white and with a circular type cut out (although I'm open to different design ideas). I've attached my logo with a circular cut out below so you can see what I'm talking about.
Should not have
• Flowers. Teddy bears. ice cream.

```html
<!DOCTYPE html>
<html lang="en">
<head>
<meta charset="utf-8">
<title>The Steadfast Fellow Show — Cover Art</title>
<link rel="stylesheet" href="https://fonts.googleapis.com/css2?family=Graduate&display=swap">
<style>
  :root {
    --stage: #c8c8c8;
    --ink: #0b0b0b;
    --paper: #ffffff;
    --photo-light: #e6e6e6;
    --photo-dark: #4a4a4a;
  }
  html, body {
    margin: 0;
    padding: 0;
    width: 1200px;
    height: 1000px;
    overflow: hidden;
    background: var(--stage);
  }
  .cover {
    position: absolute;
    left: 253px;
    top: 150px;
    width: 698px;
    height: 698px;
    background: var(--ink);
    outline: 2px solid var(--paper);
    overflow: hidden;
    font-family: "Graduate", Georgia, serif;
    color: var(--paper);
  }
  .torn-band {
    position: absolute;
    inset: 0;
    width: 698px;
    height: 698px;
  }
  .show-title {
    position: absolute;
    top: 34px;
    left: 0;
    width: 100%;
    margin: 0;
    text-align: center;
    font-weight: 400;
    font-size: 40px;
    line-height: 54px;
    letter-spacing: 2px;
  }
  .host-portrait {
    position: absolute;
    left: 170px;
    top: 150px;
    width: 356px;
    height: 356px;
    border-radius: 50%;
    border: 3px solid var(--paper);
    background: radial-gradient(circle at 50% 42%, var(--photo-light) 0%, #bdbdbd 45%, var(--photo-dark) 100%);
    box-shadow: 0 0 22px 6px rgba(0,0,0,0.35);
  }
  .brand-name {
    position: absolute;
    top: 565px;
    left: 0;
    width: 100%;
    text-align: center;
    font-size: 22px;
    letter-spacing: 4px;
  }
  .host-credit {
    position: absolute;
    top: 630px;
    left: 0;
    width: 100%;
    margin: 0;
    text-align: center;
    font-size: 30px;
    letter-spacing: 2px;
  }
</style>
</head>
<body>
  <div class="cover">
    <svg class="torn-band" viewBox="0 0 698 698" aria-hidden="true">
      <path fill="var(--paper)" d="
        M0 222 L18 216 L30 224 L48 212 L66 218 L82 206 L100 210 L118 198 L134 204
        L150 190 L170 196 L186 184 L204 190 L222 178 L240 184 L258 172 L276 178
        L296 166 L314 170 L334 160 L352 166 L372 154 L392 160 L410 148 L430 152
        L450 142 L470 148 L490 136 L510 142 L530 130 L552 136 L572 124 L594 130
        L614 120 L636 126 L656 116 L676 122 L698 112
        L698 432 L680 438 L664 430 L644 444 L626 438 L606 452 L588 446 L570 458
        L550 452 L532 466 L512 460 L494 472 L474 468 L456 480 L436 476 L416 490
        L398 484 L378 498 L358 494 L338 506 L318 500 L298 514 L278 508 L258 520
        L238 516 L218 528 L198 522 L178 536 L158 530 L138 542 L118 538 L98 550
        L78 544 L58 556 L38 550 L18 562 L0 556 Z"/>
    </svg>

    <h1 class="show-title">THE STEADFAST FELLOW<br>SHOW</h1>

    <div class="host-portrait" role="img" aria-label="Black and white portrait of host Dale Prowen, hands steepled under his chin"></div>

    <div class="brand-name">STEADFAST</div>

    <p class="host-credit">WITH DALE PROWEN</p>
  </div>
</body>
</html>
```